Talvix Inc

Hello.

I would like to take a wordpress ecomm template and turn it into a website that can display 100s of domain listings with short text box for description and a price .
One link to quorvend.example for immediate payment and with the confirmation/decline letter/email .
Five - six pages, Home, about us, domains, contact us, . Several columns or scrolling page for the domain page. I want to list several hundred virtual domains for sale .
Like a portfolio website but lists domain text .
This will be hosted on my server. On my domain.

Target Market(s)

End users, business owners, store front managers, online entpenauers , ect

Industry/Entity Type

Information Technology

Number of Pages Required

5+ page

Font styles to use
Sans Serif

Colors
0455a3
f78f20
abd036

Requirements
Must have
• Lots of white space, clean professional look . fast loading , use of greens and blues. Easy to read font.
• big headers , several - three different headers that rotate or move or clicks.
• A few current stock photos.
Should not have
• slow loading photos.
• More than two photos on any one page.

```html
<!DOCTYPE html>
<html lang="en">
<head>
<meta charset="utf-8">
<title>Talvix Inc – Premium Domains</title>
<link rel="stylesheet" href="https://fonts.googleapis.com/css2?family=Open+Sans:wght@400;600;700;800&display=swap">
<style>
:root{
  --blue:#0455a3;
  --blue-dark:#033f7a;
  --orange:#f78f20;
  --green:#abd036;
  --green-deep:#8cbf2f;
  --ink:#333;
  --muted:#777;
  --line:#e3e3e3;
  --light:#f4f5f7;
  --dark:#2b2b2b;
  --darker:#1f1f1f;
  --price:#e4572e;
}
*{box-sizing:border-box;margin:0;padding:0}
html,body{width:1200px;height:3680px;overflow:hidden}
body{font-family:"Open Sans",Arial,sans-serif;color:var(--ink);background:#fff;font-size:14px;line-height:1.5}
.wrap{width:1040px;margin:0 auto;position:relative}

/* top bar */
.topbar{height:32px;background:#f1f1f1;border-bottom:1px solid var(--line);font-size:12px;color:var(--muted)}
.topbar .wrap{display:flex;align-items:center;justify-content:space-between;height:32px}
.topbar .contact span{margin-right:24px}
.social{display:flex;gap:6px}
.social i{width:18px;height:18px;background:var(--blue);display:block;border-radius:2px}

/* header */
.header{height:112px;background:#fff}
.header .wrap{display:flex;align-items:center;justify-content:space-between;height:112px}
.brand{font-size:32px;font-weight:700;color:var(--ink)}
.nav{display:flex;align-items:center;gap:34px;font-size:14px;font-weight:600}
.nav a{color:var(--ink);text-decoration:none}
.nav a.active{color:var(--orange)}
.btn{display:inline-block;background:var(--orange);color:#fff;font-weight:700;text-decoration:none;border-radius:3px;text-transform:uppercase}
.nav .btn{padding:10px 22px;font-size:12px}

/* hero */
.hero{height:576px;position:relative;background:linear-gradient(100deg,#3a3d42 0%,#5b6168 45%,#8b9096 100%);overflow:hidden}
.hero-photo{position:absolute;right:80px;top:20px;width:520px;height:540px;background:linear-gradient(180deg,#cfd3d8 0%,#6b7178 60%,#2f3237 100%);border-radius:4px;opacity:.85}
.hero-text{position:absolute;left:80px;top:238px;color:#fff}
.hero-text h1{font-size:54px;font-weight:800;line-height:1.1;letter-spacing:1px}
.slider-arrows{position:absolute;left:80px;bottom:24px;display:flex;gap:4px}
.slider-arrows span{width:24px;height:24px;background:rgba(0,0,0,.6);display:flex;align-items:center;justify-content:center}

/* search */
.search{height:168px;background:var(--green-deep)}
.search .wrap{padding-top:28px}
.search h2{color:#fff;font-size:24px;font-weight:700;text-transform:uppercase;margin-bottom:14px}
.search form{display:flex;gap:14px}
.search .field{flex:0 0 760px;height:62px;background:#fff;border:1px solid #dcdcdc;font-size:15px;color:#999;padding:0 22px;display:flex;align-items:center}
.search .go{flex:1;height:62px;background:var(--blue);color:#fff;font-weight:700;font-size:20px;display:flex;align-items:center;justify-content:center;border-radius:3px}

/* section titles */
.sec-title{text-align:center;font-size:36px;font-weight:800;text-transform:uppercase;color:var(--ink)}
.sec-title em{font-style:normal;color:var(--blue)}
.sec-sub{text-align:center;font-size:13px;color:var(--muted);margin-top:6px}

/* services */
.services{height:312px;padding-top:40px;background:#fff}
.service-list{display:flex;justify-content:space-between;margin-top:44px}
.service{width:320px;display:flex;gap:18px}
.service .ico{flex:0 0 64px;height:64px;border:2px solid var(--orange);border-radius:50%;display:flex;align-items:center;justify-content:center}
.service h3{font-size:15px;font-weight:700;text-transform:uppercase;margin:4px 0 6px}
.service p{font-size:12px;color:var(--muted);line-height:1.6}

/* domains */
.domains{height:800px;background:var(--light);padding-top:70px}
.cards{display:grid;grid-template-columns:repeat(4,236px);gap:32px 32px;justify-content:space-between;margin-top:40px}
.card{background:#fff;border:1px solid var(--line);height:272px;text-align:center;padding:18px 18px 0;box-shadow:0 2px 4px rgba(0,0,0,.05)}
.card .badge{height:64px;margin:0 auto 18px;width:150px;border-radius:6px;background:#e9eef4}
.card h4{font-size:14px;font-weight:600;margin-bottom:6px}
.card p{font-size:11px;color:var(--muted);line-height:1.6;height:36px}
.card .price{color:var(--price);font-size:22px;font-weight:700;margin:10px 0 8px}
.card .btn{padding:6px 20px;font-size:11px;text-transform:none}
.pager{display:flex;justify-content:center;gap:6px;margin-top:44px}
.pager span{min-width:30px;height:30px;border:1px solid #d6d6d6;background:#fff;font-size:12px;display:flex;align-items:center;justify-content:center;padding:0 8px;color:var(--muted)}
.pager span.on{background:var(--green-deep);color:#fff;border-color:var(--green-deep)}

/* plans */
.plans{height:580px;padding-top:68px}
.plan-list{display:flex;justify-content:space-between;margin-top:48px}
.plan{width:304px;height:352px;border:1px solid var(--line);display:flex;flex-direction:column;text-align:center}
.plan header{height:56px;color:#fff;font-weight:700;font-size:16px;text-transform:uppercase;display:flex;align-items:center;justify-content:center}
.plan ul{list-style:none;text-align:left;padding:22px 46px 0;font-size:12px;color:var(--muted)}
.plan li{display:flex;align-items:center;gap:10px;margin-bottom:6px}
.plan .from{font-size:12px;color:var(--muted);margin-top:14px}
.plan .amount{font-size:44px;font-weight:700;line-height:1.1}
.plan footer{margin-top:auto;height:54px;color:#fff;font-weight:700;font-size:14px;text-transform:uppercase;display:flex;align-items:center;justify-content:center}
.plan.web header,.plan.web footer{background:var(--green-deep)}
.plan.cloud header,.plan.cloud footer{background:var(--orange)}
.plan.vps header,.plan.vps footer{background:var(--blue)}
.plan.web .amount{color:var(--green-deep)}
.plan.cloud .amount{color:var(--orange)}
.plan.vps .amount{color:var(--blue)}

/* promo */
.promo{height:460px;background:linear-gradient(135deg,var(--blue) 0%,var(--blue-dark) 100%);color:#fff;position:relative}
.promo .text{position:absolute;left:80px;top:120px;width:500px}
.promo h2{font-size:30px;font-weight:800;line-height:1.15;text-transform:uppercase;white-space:nowrap}
.promo p{font-size:12px;line-height:1.7;margin:16px 0 22px;color:#dce8f5}
.promo .btn{padding:9px 22px;font-size:12px;text-transform:none}
.promo .art{position:absolute;right:90px;top:60px;width:520px;height:340px;border-radius:6px;background:linear-gradient(180deg,#e9eef2 0%,#c3ccd4 70%,#8f9aa4 100%)}

/* testimonials */
.testimonials{height:240px;background:#f7f7f7;padding-top:46px}
.quotes{display:flex;justify-content:space-between}
.quote{width:480px;display:flex;gap:24px}
.quote .photo{flex:0 0 100px;height:100px;border-radius:50%;background:linear-gradient(180deg,#d9d2c9,#9a8f84)}
.stars{color:var(--orange);font-size:16px;letter-spacing:2px}
.quote p{font-size:12px;color:var(--muted);line-height:1.6;margin:4px 0 6px}
.quote .who{font-size:12px;font-weight:700;color:var(--blue)}

/* footer */
.footer{height:352px;background:var(--dark);color:#bbb;padding-top:48px}
.cols{display:flex;justify-content:space-between}
.col{width:230px}
.col h5{color:#fff;font-size:15px;font-weight:700;text-transform:uppercase;margin-bottom:16px}
.col ul{list-style:none;font-size:12px;line-height:2}
.col li::before{content:"›";color:var(--orange);margin-right:8px}
.col p{font-size:12px;line-height:1.8}
.newsletter{display:flex;margin-top:16px}
.newsletter span{flex:1;height:36px;background:#fff;font-size:11px;color:#999;padding:0 10px;display:flex;align-items:center}
.newsletter b{width:64px;height:36px;background:var(--blue);color:#fff;font-size:11px;display:flex;align-items:center;justify-content:center}
.foot-social{display:flex;gap:8px;margin-top:20px}
.foot-social i{width:30px;height:30px;background:var(--orange);border-radius:50%;display:block}
.copyright{height:48px;background:var(--darker);color:#999;font-size:12px;text-align:center;line-height:48px}
</style>
</head>
<body>

<div class="topbar">
  <div class="wrap">
    <div class="contact"><span>☏ (555) 014-2290</span><span>✉ info@talvix.example</span></div>
    <div class="social"><i></i><i></i><i></i><i></i><i></i></div>
  </div>
</div>

<header class="header">
  <div class="wrap">
    <div class="brand">Talvix Inc</div>
    <nav class="nav">
      <a class="active" href="#">HOME</a>
      <a href="#">ABOUT US</a>
      <a href="#">DOMAINS</a>
      <a href="#">BACKORDER</a>
      <a href="#">CONTACT US</a>
      <a class="btn" href="#">Special Offers</a>
    </nav>
  </div>
</header>

<section class="hero">
  <div class="hero-photo" role="img" aria-label="Photo of server racks in a data centre"></div>
  <div class="hero-text">
    <h1>TALVIX INC<br>WE SELL PREMIUM DOMAINS</h1>
  </div>
  <div class="slider-arrows">
    <span><svg width="10" height="10" viewBox="0 0 10 10"><path d="M7 1 3 5l4 4" stroke="#fff" stroke-width="2" fill="none"/></svg></span>
    <span><svg width="10" height="10" viewBox="0 0 10 10"><path d="M3 1l4 4-4 4" stroke="#fff" stroke-width="2" fill="none"/></svg></span>
  </div>
</section>

<section class="search">
  <div class="wrap">
    <h2>Start your domain name search here.</h2>
    <form>
      <div class="field">Find your perfect domain name</div>
      <div class="go">SEARCH</div>
    </form>
  </div>
</section>

<section class="services">
  <div class="wrap">
    <h2 class="sec-title">Our <em>Services</em></h2>
    <p class="sec-sub">Neque porro quisquam est qui dolorem ipsum quia dolor sit amet</p>
    <div class="service-list">
      <div class="service">
        <div class="ico"><svg width="30" height="30" viewBox="0 0 30 30" fill="none" stroke="#f78f20" stroke-width="2"><rect x="4" y="5" width="22" height="8" rx="1"/><rect x="4" y="17" width="22" height="8" rx="1"/><circle cx="9" cy="9" r="1"/><circle cx="9" cy="21" r="1"/></svg></div>
        <div><h3>Hosting</h3><p>Lorem ipsum dolor sit amet, nulla facilisi sed placerat magna vitae tempor erat dictum.</p></div>
      </div>
      <div class="service">
        <div class="ico"><svg width="30" height="30" viewBox="0 0 30 30" fill="none" stroke="#f78f20" stroke-width="2"><circle cx="15" cy="15" r="11"/><path d="M4 15h22M15 4c4 4 4 18 0 22M15 4c-4 4-4 18 0 22"/></svg></div>
        <div><h3>Domain Registration</h3><p>Lorem ipsum dolor sit amet, nulla facilisi sed placerat magna vitae tempor erat dictum.</p></div>
      </div>
      <div class="service">
        <div class="ico"><svg width="30" height="30" viewBox="0 0 30 30" fill="none" stroke="#f78f20" stroke-width="2"><rect x="4" y="8" width="22" height="15" rx="1"/><path d="M4 9l11 8 11-8"/></svg></div>
        <div><h3>Email</h3><p>Lorem ipsum dolor sit amet, nulla facilisi sed placerat magna vitae tempor erat dictum.</p></div>
      </div>
    </div>
  </div>
</section>

<section class="domains">
  <div class="wrap">
    <h2 class="sec-title">Domain <em>Listings</em></h2>
    <div class="cards">
      <div class="card"><div class="badge"></div><h4>Lorem ipsum dolor</h4><p>Neque porro quisquam est qui dolorem ipsum quia dolor sit amet.</p><div class="price">$ 190.00</div><a class="btn" href="#">Buy Now</a></div>
      <div class="card"><div class="badge"></div><h4>Lorem ipsum dolor</h4><p>Neque porro quisquam est qui dolorem ipsum quia dolor sit amet.</p><div class="price">$ 190.00</div><a class="btn" href="#">Buy Now</a></div>
      <div class="card"><div class="badge"></div><h4>Lorem ipsum dolor</h4><p>Neque porro quisquam est qui dolorem ipsum quia dolor sit amet.</p><div class="price">$ 190.00</div><a class="btn" href="#">Buy Now</a></div>
      <div class="card"><div class="badge"></div><h4>Lorem ipsum dolor</h4><p>Neque porro quisquam est qui dolorem ipsum quia dolor sit amet.</p><div class="price">$ 190.00</div><a class="btn" href="#">Buy Now</a></div>
      <div class="card"><div class="badge"></div><h4>Lorem ipsum dolor</h4><p>Neque porro quisquam est qui dolorem ipsum quia dolor sit amet.</p><div class="price">$ 190.00</div><a class="btn" href="#">Buy Now</a></div>
      <div class="card"><div class="badge"></div><h4>Lorem ipsum dolor</h4><p>Neque porro quisquam est qui dolorem ipsum quia dolor sit amet.</p><div class="price">$ 190.00</div><a class="btn" href="#">Buy Now</a></div>
      <div class="card"><div class="badge"></div><h4>Lorem ipsum dolor</h4><p>Neque porro quisquam est qui dolorem ipsum quia dolor sit amet.</p><div class="price">$ 190.00</div><a class="btn" href="#">Buy Now</a></div>
      <div class="card"><div class="badge"></div><h4>Lorem ipsum dolor</h4><p>Neque porro quisquam est qui dolorem ipsum quia dolor sit amet.</p><div class="price">$ 190.00</div><a class="btn" href="#">Buy Now</a></div>
    </div>
    <div class="pager"><span>Prev</span><span class="on">1</span><span>2</span><span>3</span><span>4</span><span>5</span><span>…</span><span>20</span><span>Next</span></div>
  </div>
</section>

<section class="plans">
  <div class="wrap">
    <h2 class="sec-title">Choose <em>Your Plan</em></h2>
    <p class="sec-sub">Nemo enim ipsam voluptatem quia voluptas sit aspernatur aut odit aut fugit</p>
    <div class="plan-list">
      <div class="plan web">
        <header>Web Hosting</header>
        <ul>
          <li><svg width="12" height="12" viewBox="0 0 12 12"><path d="M1 6l3 3 7-7" stroke="#8cbf2f" stroke-width="2" fill="none"/></svg>Unlimited disk space</li>
          <li><svg width="12" height="12" viewBox="0 0 12 12"><path d="M1 6l3 3 7-7" stroke="#8cbf2f" stroke-width="2" fill="none"/></svg>Unlimited bandwidth</li>
          <li><svg width="12" height="12" viewBox="0 0 12 12"><path d="M1 6l3 3 7-7" stroke="#8cbf2f" stroke-width="2" fill="none"/></svg>Free email accounts</li>
          <li><svg width="12" height="12" viewBox="0 0 12 12"><path d="M1 6l3 3 7-7" stroke="#8cbf2f" stroke-width="2" fill="none"/></svg>One free domain name</li>
          <li><svg width="12" height="12" viewBox="0 0 12 12"><path d="M1 6l3 3 7-7" stroke="#8cbf2f" stroke-width="2" fill="none"/></svg>Round the clock support</li>
        </ul>
        <div class="from">Starting at</div>
        <div class="amount">$1000</div>
        <footer>Get Started</footer>
      </div>
      <div class="plan cloud">
        <header>Cloud Hosting</header>
        <ul>
          <li><svg width="12" height="12" viewBox="0 0 12 12"><path d="M1 6l3 3 7-7" stroke="#f78f20" stroke-width="2" fill="none"/></svg>Unlimited disk space</li>
          <li><svg width="12" height="12" viewBox="0 0 12 12"><path d="M1 6l3 3 7-7" stroke="#f78f20" stroke-width="2" fill="none"/></svg>Unlimited bandwidth</li>
          <li><svg width="12" height="12" viewBox="0 0 12 12"><path d="M1 6l3 3 7-7" stroke="#f78f20" stroke-width="2" fill="none"/></svg>Free email accounts</li>
          <li><svg width="12" height="12" viewBox="0 0 12 12"><path d="M1 6l3 3 7-7" stroke="#f78f20" stroke-width="2" fill="none"/></svg>One free domain name</li>
          <li><svg width="12" height="12" viewBox="0 0 12 12"><path d="M1 6l3 3 7-7" stroke="#f78f20" stroke-width="2" fill="none"/></svg>Round the clock support</li>
        </ul>
        <div class="from">Starting at</div>
        <div class="amount">$1500</div>
        <footer>Get Started</footer>
      </div>
      <div class="plan vps">
        <header>VPS Hosting</header>
        <ul>
          <li><svg width="12" height="12" viewBox="0 0 12 12"><path d="M1 6l3 3 7-7" stroke="#0455a3" stroke-width="2" fill="none"/></svg>Unlimited disk space</li>
          <li><svg width="12" height="12" viewBox="0 0 12 12"><path d="M1 6l3 3 7-7" stroke="#0455a3" stroke-width="2" fill="none"/></svg>Unlimited bandwidth</li>
          <li><svg width="12" height="12" viewBox="0 0 12 12"><path d="M1 6l3 3 7-7" stroke="#0455a3" stroke-width="2" fill="none"/></svg>Free email accounts</li>
          <li><svg width="12" height="12" viewBox="0 0 12 12"><path d="M1 6l3 3 7-7" stroke="#0455a3" stroke-width="2" fill="none"/></svg>One free domain name</li>
          <li><svg width="12" height="12" viewBox="0 0 12 12"><path d="M1 6l3 3 7-7" stroke="#0455a3" stroke-width="2" fill="none"/></svg>Round the clock support</li>
        </ul>
        <div class="from">Starting at</div>
        <div class="amount">$1200</div>
        <footer>Get Started</footer>
      </div>
    </div>
  </div>
</section>

<section class="promo">
  <div class="text">
    <h2>Talvix Inc<br>We sell premium domains</h2>
    <p>Lorem Ipsum has been the industry's standard dummy text ever since the 1500s, when an unknown printer took a galley of type and scrambled it to make a type specimen book. It has survived not only five centuries, but also the leap into electronic typesetting, remaining essentially unchanged.</p>
    <a class="btn" href="#">Read more</a>
  </div>
  <div class="art" role="img" aria-label="Illustration of a laptop showing a secure website address with a magnifying glass"></div>
</section>

<section class="testimonials">
  <div class="wrap">
    <div class="quotes">
      <div class="quote">
        <div class="photo" role="img" aria-label="Portrait photo of a male customer"></div>
        <div><div class="stars">★★★★☆</div><p>Lorem Ipsum has been the industry's standard dummy text ever since the 1500s, when an unknown printer took a galley of type and made a book.</p><div class="who">Daniel Moreno</div></div>
      </div>
      <div class="quote">
        <div class="photo" role="img" aria-label="Portrait photo of a female customer"></div>
        <div><div class="stars">★★★★☆</div><p>Lorem Ipsum has been the industry's standard dummy text ever since the 1500s, when an unknown printer took a galley of type and made a book.</p><div class="who">Clara Whitfield</div></div>
      </div>
    </div>
  </div>
</section>

<footer class="footer">
  <div class="wrap cols">
    <div class="col">
      <h5>Links</h5>
      <ul><li>Customer Support</li><li>Knowledgebase</li><li>Resources</li><li>Network Status</li><li>Domain Help</li><li>Affiliates</li></ul>
    </div>
    <div class="col">
      <h5>Hosting</h5>
      <p>Lorem ipsum has been the industry's standard dummy text ever since the 1500s, when an unknown printer took a galley of type and scrambled it to make a specimen book for all.</p>
    </div>
    <div class="col">
      <h5>Get in Touch</h5>
      <p>Address: 48 Harbor Lane,<br>Westbrook, ST 00000<br>Phone: (555) 014-2290<br>Fax: (555) 014-2291<br>Email: info@talvix.example</p>
    </div>
    <div class="col">
      <h5>Newsletter</h5>
      <p>Sign up to receive news and offers straight to your inbox.</p>
      <div class="newsletter"><span>Your email address</span><b>Submit</b></div>
      <div class="foot-social"><i></i><i></i><i></i></div>
    </div>
  </div>
</footer>
<div class="copyright">Copyright © 2016. All Rights Reserved.</div>

</body>
</html>
```